Criação de Papelaria Profissional para Beleza
A empresa queria:
" Espaço físico tipo loja com cabines exclusivas para depilação, método Espanhol com cera quente. Única com cauterização pós depilação. E espaço dedicado a beleza das mãos e pés "

```html
<!DOCTYPE html>
<html lang="pt-BR">
<head>
<meta charset="utf-8">
<title>Florenza — Pasta de Apresentação</title>
<link href="https://fonts.googleapis.com/css2?family=Montserrat:wght@400;600&display=swap" rel="stylesheet">
<style>
  :root {
    --backdrop: #e9e6e3;
    --paper: #f7f7f7;
    --plum: #2e2228;
    --pink: #d8327f;
    --ink: #6d6a6c;
  }
  * { margin: 0; padding: 0; box-sizing: border-box; }
  html, body { width: 1200px; height: 1200px; overflow: hidden; }
  body {
    background: var(--backdrop);
    display: flex;
    align-items: center;
    justify-content: center;
    font-family: "Montserrat", sans-serif;
  }
  .folder-spread {
    display: flex;
    width: 960px;
    height: 640px;
    box-shadow: 0 10px 30px rgba(0,0,0,0.12);
    position: relative;
  }
  .folder-spread::after {
    content: "";
    position: absolute;
    left: 0; right: 0; bottom: 0;
    height: 9px;
    background: var(--pink);
  }
  .panel { width: 50%; height: 100%; position: relative; }
  .back-panel { background: var(--paper); }
  .front-panel {
    background: var(--plum);
    display: flex;
    align-items: center;
    justify-content: center;
  }
  .brand {
    display: flex;
    align-items: center;
    gap: 14px;
    color: var(--pink);
    font-weight: 600;
    white-space: nowrap;
  }
  .brand-dot {
    width: 14px; height: 14px;
    border-radius: 50%;
    background: var(--pink);
    flex: none;
  }
  .front-panel .brand { font-size: 46px; letter-spacing: 1px; margin-top: -20px; }
  .back-panel .brand {
    position: absolute;
    left: 240px;
    bottom: 62px;
    font-size: 22px;
    gap: 8px;
  }
  .back-panel .brand-dot { width: 8px; height: 8px; }
  .contact-list {
    position: absolute;
    left: 26px;
    bottom: 40px;
    list-style: none;
    display: flex;
    flex-direction: column;
    gap: 7px;
  }
  .contact-item {
    display: flex;
    align-items: center;
    gap: 7px;
    font-size: 10px;
    color: var(--ink);
    white-space: nowrap;
  }
  .contact-icon {
    width: 13px; height: 13px;
    border-radius: 50%;
    background: var(--pink);
    display: flex; align-items: center; justify-content: center;
    flex: none;
  }
  .contact-icon svg { width: 8px; height: 8px; }
</style>
</head>
<body>
  <div class="folder-spread">
    <section class="panel back-panel">
      <ul class="contact-list">
        <li class="contact-item">
          <span class="contact-icon"><svg viewBox="0 0 10 10"><path d="M2 1 L4 1 L4.6 3 L3.5 3.8 Q4.5 5.8 6.2 6.5 L7 5.4 L9 6 L9 8 Q5 9 2.3 5.8 Q1 3.8 2 1Z" fill="#fff"/></svg></span>
          (11) 4000-1234
        </li>
        <li class="contact-item">
          <span class="contact-icon"><svg viewBox="0 0 10 10"><rect x="1" y="2.5" width="8" height="5" fill="none" stroke="#fff"/><path d="M1 2.5 L5 5.5 L9 2.5" fill="none" stroke="#fff"/></svg></span>
          contato@florenza.com
        </li>
        <li class="contact-item">
          <span class="contact-icon"><svg viewBox="0 0 10 10"><circle cx="5" cy="5" r="3.8" fill="none" stroke="#fff"/><path d="M1.2 5 H8.8 M5 1.2 Q2.8 5 5 8.8 M5 1.2 Q7.2 5 5 8.8" fill="none" stroke="#fff" stroke-width="0.8"/></svg></span>
          www.florenza.com
        </li>
        <li class="contact-item">
          <span class="contact-icon"><svg viewBox="0 0 10 10"><path d="M5 9 Q1.5 5 1.8 3.6 A3.2 3.2 0 0 1 8.2 3.6 Q8.5 5 5 9Z" fill="#fff"/><circle cx="5" cy="3.8" r="1.1" fill="#d8327f"/></svg></span>
          Rua das Flores, 120 - Centro
        </li>
      </ul>
      <div class="brand"><span class="brand-dot"></span>Florenza</div>
    </section>
    <section class="panel front-panel">
      <div class="brand"><span class="brand-dot"></span>Florenza</div>
    </section>
  </div>
</body>
</html>
```